Etiketten für Honiggläser
Zielgruppe
Ich bin ein Imker und möchte meine Honig verkaufen.
Aufgabenstellung
Ich möchte exklusive und edle Honigetiketten die auffallen. Bevorzugt mit den Farben Gold und Schwarz. Ich habe weder ein Logo noch hat meine Imkerei einen Namen. ( Vorschläge sind aber auch willkommen ).
Auf die Vorderseite des Honigetiketts soll zu lesen sein:
- Deutscher Honig
- Sommertracht
- 500g
Auf der Rückseite des Honigetiketts soll zu finden sein:
- Namen und Adresse des Imkers
- freies Feld für das Mindesthaltbarkeitsdatum
Ergänzende Informationen:
- Name: Tobias Wenkel
- Adresse: Lindenpfad 47, 82140 Olching ( Bayern )
Habe mir ein Design in dieser Richtung vorgestellt:
https://cdn.bildablage-beispiel.de/media/honig-vorlage-01.jpg
https://www.vektorfundus-beispiel.de/de/vektor/honig-elemente-schwarz-4471

```html
<!DOCTYPE html>
<html lang="de">
<head>
<meta charset="utf-8">
<title>Honigetiketten – Vorderseite und Rückseite</title>
<link href="https://fonts.googleapis.com/css2?family=Playfair+Display:wght@800&family=Roboto:wght@400&family=Nothing+You+Could+Do&display=swap" rel="stylesheet">
<style>
  :root {
    --page: #ffffff;
    --navy: #0b1220;
    --navy-deep: #050a14;
    --gold: #c4a468;
    --gold-soft: #b8985c;
  }
  * { box-sizing: border-box; margin: 0; padding: 0; }
  html, body {
    width: 1200px;
    height: 1200px;
    overflow: hidden;
    background: var(--page);
  }
  .sheet {
    position: relative;
    width: 1200px;
    height: 1200px;
    display: flex;
    align-items: center;
    justify-content: center;
    gap: 28px;
  }
  .label {
    position: relative;
    width: 560px;
    height: 446px;
    background: var(--navy);
    overflow: hidden;
  }
  .label__pattern {
    position: absolute;
    inset: 0;
    background: radial-gradient(circle at 50% 50%, #111a2c 0%, var(--navy) 70%);
  }
  .label__panel {
    position: absolute;
    background: var(--navy-deep);
    border: 5px solid var(--gold);
  }
  .label--front .label__panel { left: 18%; top: 16%; width: 68%; height: 64%; }
  .label--back  .label__panel { left: 17%; top: 16%; width: 68%; height: 64%; }
  .label__inner-frame {
    position: absolute;
    inset: 10px;
    border: 2px solid var(--gold);
    display: flex;
    flex-direction: column;
    align-items: center;
    justify-content: center;
    color: var(--gold);
  }
  .brand-name {
    font-family: "Roboto", sans-serif;
    font-weight: 400;
    font-size: 30px;
    letter-spacing: 1px;
    color: var(--gold);
  }
  .product-title {
    font-family: "Playfair Display", serif;
    font-weight: 800;
    font-size: 31px;
    letter-spacing: -0.5px;
    margin-top: 22px;
    line-height: 1;
  }
  .product-origin {
    font-family: "Nothing You Could Do", cursive;
    font-size: 17px;
    align-self: flex-end;
    margin-right: 24px;
    margin-top: 4px;
  }
  .net-weight {
    position: absolute;
    right: 12px;
    bottom: 10px;
    font-family: "Roboto", sans-serif;
    font-size: 10px;
  }
  .beekeeper-address {
    font-family: "Roboto", sans-serif;
    font-size: 13px;
    line-height: 1.35;
    text-align: center;
    margin-top: 26px;
  }
  .best-before-field {
    width: 152px;
    height: 25px;
    background: var(--gold-soft);
    margin-top: 24px;
  }
</style>
</head>
<body>
<main class="sheet">
  <section class="label label--front" aria-label="Etikett Vorderseite">
    <div class="label__pattern" role="img" aria-label="Goldenes Wabenmuster mit Sechsecken auf dunklem Blau"></div>
    <div class="label__panel">
      <div class="label__inner-frame">
        <p class="brand-name">Tobias Wenkel</p>
        <h1 class="product-title">SOMMERTRACHT</h1>
        <p class="product-origin">deutscher Honig</p>
        <p class="net-weight">500g</p>
      </div>
    </div>
  </section>

  <section class="label label--back" aria-label="Etikett Rückseite">
    <div class="label__pattern" role="img" aria-label="Goldenes Wabenmuster mit Sechsecken auf dunklem Blau"></div>
    <div class="label__panel">
      <div class="label__inner-frame">
        <p class="brand-name">Tobias Wenkel</p>
        <p class="beekeeper-address">Lindenpfad 47<br>DE - 82999 Wabenfeld</p>
        <div class="best-before-field" aria-label="Feld für Mindesthaltbarkeitsdatum"></div>
      </div>
    </div>
  </section>
</main>
</body>
</html>
```